Product labels for new supplements business targeting high performing creative people

I need a label design for different supplements like Whey, BCAA, Melatonin etc. that I could customize for each use case separately.

The brand is called wovenpath.life, and it would be the first design of the labels. We haven't sold any products yet, but the target audience is people with growth mindset, people who want to be as efficient as possible and are constantly looking to improve their lifestyle. As part of that, they are also working out, but don't know much about supplements yet. Mostly people between 20-34.

I don't have a too specific idea of the expected design, though it should be light, warm, smart and minimalist, maybe have some patterns. It should looks smart and clean (and expensive). Orange and golden might be the additional colors for white. I have attached the templates of some products that I plan to sell and also the logo of the brand.

Here's what I have used for inspiration:
Brands that I like and are somewhat similar in concept: https://www.plarnix.com/ (!!specially the way they
bring "how the product helps them" in focus, not "what the product is" & https://www.bevo.care/ &
https://www.moflesta.com/sport/ & https://en.calwostor.fr/ &
https://artboardhub.com/profiles/mirelfondastudio/designs/461827

Here's how different products look like: https://bondrexa.com/catalog

Target Market(s)

target audience is people with growth mindset, people who want to be as efficient as possible and are constantly looking to improve their lifestyle. As part of that, they are also working out, but don't know much about supplements yet. Mostly people between 20-34.

Industry/Entity Type

Supplements

Font styles to use
Sans Serif

Colors
FFC000
F8CF3A
FAE287
FDF2CF
FEFAEE
F0912C
F2A743
F7CA91
FBE8D2
FDF5EE
EE7325
F08F49
F5BC92
FAE3D3
FDF4ED

Requirements
Must have
• Clean, smart and minimalist design that can be applied for different products in different sizes, like Whey protein, BCAA, vitamins etc. available here: https://bondrexa.com/catalog
Nice to have
• Patterns, expensive look
Should not have
• Doodles, too many colors

```html
<!DOCTYPE html>
<html lang="en">
<head>
<meta charset="utf-8">
<title>wovenpath.life – supplement labels</title>
<link href="https://fonts.googleapis.com/css2?family=Montserrat:wght@800&family=Poppins:wght@300;400;500;600&display=swap" rel="stylesheet">
<style>
  :root {
    --canvas-bg: #f2f2f2;
    --label-bg: #ffffff;
    --gold-dark: #c39a22;
    --gold-mid: #d8b43c;
    --gold-light: #ecd57a;
    --gold-text: #d2a93a;
    --orange: #ee7325;
    --ink: #2b2b2b;
    --grey: #7d7d7d;
    --brown-grey: #8a7a6a;
    --logo-dot: #ee7325;
  }
  * { box-sizing: border-box; margin: 0; padding: 0; }
  html, body { width: 1092px; height: 1200px; overflow: hidden; }
  body { background: var(--canvas-bg); font-family: "Poppins", sans-serif; position: relative; }

  .label-sheet {
    position: absolute; left: 30px; top: 326px;
    display: grid; grid-template-columns: 500px 500px; gap: 40px 32px;
  }
  .label {
    position: relative; width: 500px; height: 254px;
    background: var(--label-bg); overflow: hidden;
    box-shadow: 0 2px 8px rgba(0,0,0,0.12);
  }
  .label-body { position: absolute; top: 0; bottom: 0; left: var(--shift, 0px); width: 500px; }

  .gold-curve { position: absolute; left: 0; top: 0; width: 500px; height: 254px; }

  .product-title {
    position: absolute; left: 177px; bottom: 15px;
    writing-mode: vertical-rl; transform: rotate(180deg);
    font-family: "Montserrat", sans-serif; font-weight: 800;
    font-size: var(--title-size, 33px); line-height: 1; letter-spacing: 0.5px;
    background: linear-gradient(90deg, var(--gold-dark), var(--gold-light) 55%, var(--gold-mid));
    -webkit-background-clip: text; background-clip: text; color: transparent;
    white-space: nowrap;
  }
  .product-variant {
    position: absolute; left: 214px; bottom: 15px;
    writing-mode: vertical-rl; transform: rotate(180deg);
    font-size: 15px; font-weight: 400; line-height: 1; white-space: nowrap;
  }
  .variant-grey { color: var(--grey); }
  .variant-brown { color: var(--brown-grey); }
  .variant-orange { color: var(--orange); }

  .brand {
    position: absolute; left: 230px; top: 20px;
    display: flex; align-items: center; gap: 6px;
    font-size: 16.5px; font-weight: 500; color: var(--ink); letter-spacing: 0.2px;
  }
  .brand-dot { width: 13px; height: 13px; border-radius: 50%; background: var(--logo-dot); }

  .benefits {
    position: absolute; right: 156px; top: var(--benefits-top, 120px);
    list-style: none; text-align: right;
    font-size: 9px; font-weight: 300; color: var(--grey); line-height: 1.15;
  }
  .benefits li { margin-bottom: 6px; }
  .benefits li::before { content: "•"; color: var(--gold-mid); margin-right: 3px; }

  .divider-wave { position: absolute; right: 156px; top: 174px; width: 76px; height: 10px; }

  .supplement-tag {
    position: absolute; right: 156px; top: 190px; text-align: right;
    font-size: 11.5px; font-weight: 600; letter-spacing: 2px; line-height: 1.3;
    color: var(--gold-text);
  }
  .net-content {
    position: absolute; right: 156px; top: 226px;
    font-size: 9.5px; font-weight: 400; color: var(--grey);
  }
</style>
</head>
<body>
<main class="label-sheet">

  <section class="label" style="--shift:0px; --title-size:33px; --benefits-top:118px;">
    <div class="label-body">
      <svg class="gold-curve" viewBox="0 0 500 254" aria-hidden="true">
        <defs><linearGradient id="g1" x1="0" y1="0" x2="0" y2="1"><stop offset="0" stop-color="#c39a22"/><stop offset="0.5" stop-color="#ecd57a"/><stop offset="1" stop-color="#c39a22"/></linearGradient></defs>
        <path d="M159 0 C170 40 168 90 158 140 S146 230 162 254" fill="none" stroke="url(#g1)" stroke-width="2.2"/>
      </svg>
      <h2 class="product-title">MELATONIN</h2>
      <span class="product-variant variant-grey">1 mg</span>
      <div class="brand"><span class="brand-dot"></span>wovenpath.life</div>
      <ul class="benefits"><li>Stay asleep longer</li><li>Fall asleep faster</li></ul>
      <svg class="divider-wave" viewBox="0 0 76 10" aria-hidden="true"><path d="M1 6 C20 0 40 10 75 4" fill="none" stroke="#d2a93a" stroke-width="1"/></svg>
      <p class="supplement-tag">DIETARY<br>SUPPLEMENT</p>
      <p class="net-content">60 tablets</p>
    </div>
  </section>

  <section class="label" style="--shift:-18px; --title-size:26px; --benefits-top:112px;">
    <div class="label-body">
      <svg class="gold-curve" viewBox="0 0 500 254" aria-hidden="true">
        <defs><linearGradient id="g2" x1="0" y1="0" x2="0" y2="1"><stop offset="0" stop-color="#c39a22"/><stop offset="0.5" stop-color="#ecd57a"/><stop offset="1" stop-color="#c39a22"/></linearGradient></defs>
        <path d="M159 0 C170 40 168 90 158 140 S146 230 162 254" fill="none" stroke="url(#g2)" stroke-width="2.2"/>
      </svg>
      <h2 class="product-title">BEFF PROTEIN</h2>
      <span class="product-variant variant-brown">chocolate</span>
      <div class="brand"><span class="brand-dot"></span>wovenpath.life</div>
      <ul class="benefits"><li>Hydrolized beef protein with<br>minimum fat content</li><li>Promotes muscle gain and<br>help maintain muscle mass</li></ul>
      <svg class="divider-wave" viewBox="0 0 76 10" aria-hidden="true"><path d="M1 6 C20 0 40 10 75 4" fill="none" stroke="#d2a93a" stroke-width="1"/></svg>
      <p class="supplement-tag">DIETARY<br>SUPPLEMENT</p>
      <p class="net-content">Net Wt. 900 g (31.75 oz)</p>
    </div>
  </section>

  <section class="label" style="--shift:-2px; --title-size:32px; --benefits-top:114px;">
    <div class="label-body">
      <svg class="gold-curve" viewBox="0 0 500 254" aria-hidden="true">
        <defs><linearGradient id="g3" x1="0" y1="0" x2="0" y2="1"><stop offset="0" stop-color="#c39a22"/><stop offset="0.5" stop-color="#ecd57a"/><stop offset="1" stop-color="#c39a22"/></linearGradient></defs>
        <path d="M159 0 C170 40 168 90 158 140 S146 230 162 254" fill="none" stroke="url(#g3)" stroke-width="2.2"/>
      </svg>
      <h2 class="product-title">MACA ROOT</h2>
      <span class="product-variant variant-orange">powder</span>
      <div class="brand"><span class="brand-dot"></span>wovenpath.life</div>
      <ul class="benefits"><li>Help reduce stress</li><li>Increaces energy<br>and stamina</li></ul>
      <svg class="divider-wave" viewBox="0 0 76 10" aria-hidden="true"><path d="M1 6 C20 0 40 10 75 4" fill="none" stroke="#d2a93a" stroke-width="1"/></svg>
      <p class="supplement-tag">DIETARY<br>SUPPLEMENT</p>
      <p class="net-content">20 mg</p>
    </div>
  </section>

  <section class="label" style="--shift:-18px; --title-size:33px; --benefits-top:96px;">
    <div class="label-body">
      <svg class="gold-curve" viewBox="0 0 500 254" aria-hidden="true">
        <defs><linearGradient id="g4" x1="0" y1="0" x2="0" y2="1"><stop offset="0" stop-color="#c39a22"/><stop offset="0.5" stop-color="#ecd57a"/><stop offset="1" stop-color="#c39a22"/></linearGradient></defs>
        <path d="M159 0 C170 40 168 90 158 140 S146 230 162 254" fill="none" stroke="url(#g4)" stroke-width="2.2"/>
      </svg>
      <h2 class="product-title">BCAA 2:1:1</h2>
      <span class="product-variant variant-orange">wild berry</span>
      <div class="brand"><span class="brand-dot"></span>wovenpath.life</div>
      <ul class="benefits"><li>Essencial branshed chain<br>amino acids BCAA</li><li>Increaces mucle growth,<br>reduces fatique</li></ul>
      <svg class="divider-wave" viewBox="0 0 76 10" aria-hidden="true"><path d="M1 6 C20 0 40 10 75 4" fill="none" stroke="#d2a93a" stroke-width="1"/></svg>
      <p class="supplement-tag">DIETARY<br>SUPPLEMENT</p>
      <p class="net-content">Net Wt. 300 g (10.58 oz)</p>
    </div>
  </section>

</main>
</body>
</html>
```